New College Graduate Resume - Creative and unique design that stands out from the rest

Need creative resume design for recent college graduate who graduated from School of Music with a concentration in music composition and production. Striving for a contemporary layout/design that allows the resume to "be unique" and "stand out" but be polished and professional. Open to integrating moderate color/graphics as part of resume design but the design can be minus those attributes as well. Attached is raw content in 7 sections (name/contact info, education, highlights of qualifications, work experience, honors/awards, and professional affiliations). While the designer has full latitude over overall design which (section headers, font type, separation/spacing, use of bullets, justification of text, etc.) please maintain current order/sequence of the 7 sections.

Industry/Entity Type

School

Requirements
Must have
• Name (Tobias Hale Whitcombe II) should be most prominent (bold/font size) compared to remainder of resume copy.
• Section headers should be prominent but less so when compared to name on resume.
• The attached file of resume content is provided as raw source copy and is NOT to be just copied and pasted into open fields as is. Expectation is each section of copy will be organized in a manner that is most visually appealing and may include bullets, appropriate spacing, etc.
Should not have
• The attached file of resume content is provided as source copy and is NOT to be just copied and pasted into open fields as is. Expectation is each section of copy will be organized in a manner that

```html
<!DOCTYPE html>
<html lang="en">
<head>
<meta charset="utf-8">
<title>Tobias Hale Whitcombe II – Résumé</title>
<link rel="stylesheet" href="https://fonts.googleapis.com/css2?family=Oswald:wght@400;500;600;700&family=Pathway+Gothic+One&display=swap">
<style>
:root{
  --ink:#1f1f1f;
  --body:#2b2b2b;
  --orange:#f5823c;
  --sidebar:#121212;
  --sidebar-text:#ffffff;
  --muted:#d8d8d8;
  --paper:#ffffff;
}
*{margin:0;padding:0;box-sizing:border-box}
html,body{width:927px;height:1200px;overflow:hidden;background:var(--paper)}
.resume{position:relative;width:927px;height:1200px;overflow:hidden;background:var(--paper);font-family:"Pathway Gothic One",sans-serif;color:var(--body)}

/* header artwork area */
.header-art{position:absolute;left:301px;top:0;width:626px;height:190px;
  background:radial-gradient(circle at 30% 45%,#cfcfcf 0,#e9e9e9 22%,#f7f7f7 45%,#fff 70%),
             radial-gradient(circle at 75% 20%,#dcdcdc 0,#fff 40%);}

/* sidebar */
.sidebar{position:absolute;left:23px;top:0;width:252px;height:1200px;background:var(--sidebar);color:var(--sidebar-text)}
.sidebar-texture{position:absolute;inset:0;background:radial-gradient(ellipse at 50% 50%,#3a3a3a 0,#1b1b1b 35%,#111 70%);opacity:.9}
.accent-strip{position:absolute;left:275px;top:0;width:26px;height:1200px;background:var(--orange)}
.pointer{position:absolute;left:300px;width:0;height:0;border-top:17px solid transparent;border-bottom:17px solid transparent;border-left:14px solid var(--orange)}

.contact{position:absolute;left:0;top:40px;width:252px}
.contact-row{position:absolute;left:52px;display:flex;align-items:center;font-family:"Oswald",sans-serif;color:#fff}
.contact-icon{position:absolute;left:-40px}
.phone{top:0;font-size:26px;font-weight:500;letter-spacing:.3px}
.email{top:45px;font-size:15.5px;font-weight:500}
.address{top:85px;font-size:14px;line-height:22px;letter-spacing:.4px}

.side-heading{position:absolute;left:33px;font-family:"Oswald",sans-serif;font-weight:600;font-size:20px;color:var(--orange);letter-spacing:.2px}
.skills-heading{top:222px}
.skills{position:absolute;left:33px;top:266px;list-style:none;font-family:"Oswald",sans-serif;font-variant:small-caps;font-size:18px;line-height:30.2px;letter-spacing:.2px}
.skills .sub{font-style:italic;font-variant:normal;padding-left:10px;font-size:17px}

.edu-heading{top:780px}
.education{position:absolute;left:33px;top:822px;font-family:"Oswald",sans-serif}
.school{font-size:18.5px;font-weight:500;line-height:24px}
.school .sc{font-variant:small-caps}
.edu-line{font-family:"Pathway Gothic One",sans-serif;font-size:16px;line-height:19px;color:var(--muted);letter-spacing:.4px}
.degree{font-size:18.5px;font-weight:500;line-height:24px}
.edu-block+.edu-block{margin-top:22px}

.sidebar-icons{position:absolute;left:12px;top:1110px;display:flex;gap:22px;align-items:center}

/* main column */
.name{position:absolute;left:345px;top:62px;font-family:"Oswald",sans-serif;font-weight:600;font-size:45px;line-height:1;color:var(--ink);white-space:nowrap;letter-spacing:-.5px}
.name .accent{color:var(--orange)}
.title{position:absolute;right:47px;top:150px;font-family:"Oswald",sans-serif;font-size:20px;font-weight:500;color:var(--ink)}
.title .accent{color:var(--orange)}

.section-heading{position:absolute;left:337px;font-family:"Oswald",sans-serif;font-weight:600;font-size:21px;color:var(--orange);line-height:1}
.profile-text{position:absolute;left:371px;top:251px;width:518px;font-size:17px;line-height:23.5px;letter-spacing:.3px}

.bullets{list-style:none;font-size:16.5px;line-height:22.4px;letter-spacing:.3px}
.bullets li{position:relative;padding-left:17px}
.bullets li::before{content:"";position:absolute;left:3px;top:8px;width:7px;height:7px;background:var(--body);transform:rotate(45deg)}
.honors{position:absolute;left:375px;top:437px}
.affiliations{position:absolute;left:375px;top:569px}

.job{position:absolute;left:371px;width:515px}
.job-head{display:flex;justify-content:space-between;font-family:"Oswald",sans-serif;font-size:13.5px;line-height:18px;margin-bottom:6px}
.job-title{font-weight:600;color:var(--ink);text-transform:uppercase}
.job-place{text-decoration:underline;text-transform:uppercase;letter-spacing:.2px}
.job-place small{font-size:11.5px}
.job-text{font-size:16.5px;line-height:23px;letter-spacing:.3px}
.job .bullets{margin-left:4px}
.sc-text{font-variant:small-caps}
</style>
</head>
<body>
<main class="resume">
  <div class="header-art" role="img" aria-label="Soft grey speaker and sound wave artwork"></div>

  <aside class="sidebar">
    <div class="sidebar-texture" role="img" aria-label="Faint sound wave pattern on dark background"></div>

    <div class="contact">
      <div class="contact-row phone">
        <svg class="contact-icon" width="16" height="22" viewBox="0 0 16 22"><rect x="1.5" y="1.5" width="13" height="19" rx="2" fill="none" stroke="#f5823c" stroke-width="2.5"/><rect x="6" y="16" width="4" height="2" fill="#f5823c"/></svg>
        470-555-0182
      </div>
      <div class="contact-row email">
        <svg class="contact-icon" width="18" height="13" viewBox="0 0 18 13"><rect x="1" y="1" width="16" height="11" fill="none" stroke="#f5823c" stroke-width="2"/><path d="M1 1l8 6 8-6" fill="none" stroke="#f5823c" stroke-width="2"/></svg>
        thwhitcombe@mailbox.net
      </div>
      <div class="contact-row address">
        <svg class="contact-icon" style="top:2px" width="14" height="20" viewBox="0 0 14 20"><path d="M7 0C3 0 0 3 0 7c0 5 7 13 7 13s7-8 7-13c0-4-3-7-7-7z" fill="#f5823c"/><circle cx="7" cy="7" r="2.6" fill="#121212"/></svg>
        <div>218 Larkspur Lane<br>Atlanta, Georgia&nbsp; 30318</div>
      </div>
    </div>

    <h2 class="side-heading skills-heading">SKILLS &amp; SCOPE</h2>
    <ul class="skills">
      <li>Media Production</li>
      <li>Software</li>
      <li class="sub">(Studio Suite 11)</li>
      <li>Sound Design</li>
      <li>Sound Acoustics</li>
      <li>Studio Recording</li>
      <li>Audio Editing</li>
      <li>Audio Mixing</li>
      <li>Analog/Digital Board</li>
      <li>Operation</li>
      <li>Music Arranging</li>
      <li>Music Composition</li>
      <li>Music Production</li>
      <li>Composing Sheet Music</li>
      <li>Singer-songwriter</li>
      <li>Rhythm guitarist</li>
    </ul>

    <h2 class="side-heading edu-heading">EDUCATION</h2>
    <div class="education">
      <div class="edu-block">
        <div class="school">CORAL BAY UNIVERSITY</div>
        <div class="school"><span class="sc">Hartwell School of Music</span></div>
        <div class="edu-line">Coral Springs, Florida</div>
        <div class="degree">B.A. MUSIC - MAY 2016</div>
        <div class="edu-line">Major: Media Writing and<br>Production, GPA 3.20/4.0</div>
      </div>
      <div class="edu-block">
        <div class="school">LINDEN RIDGE ACADEMY</div>
        <div class="edu-line">College Park, Georgia<br>High School Diploma<br>with Honors – May 2011</div>
      </div>
    </div>

    <div class="sidebar-icons">
      <svg width="26" height="22" viewBox="0 0 26 22"><rect x="1" y="1" width="24" height="20" fill="none" stroke="#fff" stroke-width="2"/><path d="M7 1v20M13 1v20M19 1v20" stroke="#fff" stroke-width="2"/><path d="M7 1v11M13 1v11M19 1v11" stroke="#fff" stroke-width="5"/></svg>
      <svg width="24" height="24" viewBox="0 0 24 24"><path d="M3 0v24M9 0v24M15 0v24M21 0v24" stroke="#fff" stroke-width="2"/><path d="M0 8h6M6 15h6M12 6h6M18 12h6" stroke="#fff" stroke-width="3"/></svg>
      <svg width="26" height="26" viewBox="0 0 26 26"><circle cx="13" cy="13" r="11" fill="none" stroke="#fff" stroke-width="2"/><path d="M8 13h10" stroke="#fff" stroke-width="2.5"/></svg>
      <svg width="26" height="22" viewBox="0 0 26 22"><path d="M2 22V8a3 3 0 0 1 6 0v6a3 3 0 0 0 6 0V8a3 3 0 0 1 6 0v6a3 3 0 0 0 6 0" fill="none" stroke="#fff" stroke-width="2.5"/></svg>
      <svg width="24" height="22" viewBox="0 0 24 22"><path d="M3 22V11M9 22V4M15 22V11M21 22V4" stroke="#fff" stroke-width="3"/><circle cx="3" cy="6" r="1.8" fill="#fff"/><circle cx="15" cy="6" r="1.8" fill="#fff"/></svg>
    </div>
  </aside>

  <div class="accent-strip"></div>
  <span class="pointer" style="top:86px"></span>
  <span class="pointer" style="top:217px"></span>
  <span class="pointer" style="top:403px"></span>
  <span class="pointer" style="top:535px"></span>
  <span class="pointer" style="top:668px"></span>

  <h1 class="name">TOBIAS <span class="accent">HALE WHITCOMBE II</span></h1>
  <p class="title"><span class="accent">MUSIC</span> Production &amp; Composition</p>

  <h2 class="section-heading" style="top:224px">PROFILE</h2>
  <p class="profile-text">Recent graduate of a highly ranked university seeking opportunities to apply composition and production talents across a variety of music genres and other media. Expertise lies in delivering high quality sound design, editing, mixing, and recording. Excellent interpersonal skills and the ability to build strong relationships with people at all levels.&nbsp; Exceptionally motivated self-starter and creative problem solver who enjoys working collaboratively on teams.</p>

  <h2 class="section-heading" style="top:410px">HONORS/AWARDS</h2>
  <ul class="bullets honors">
    <li>Best Film and Score: Frights and Frames 2015 Competition (Coral Bay University)</li>
    <li>Edwin P. Marsh Scholar</li>
    <li>Best New Member, Delta Kappa Rho Fraternity, Inc.</li>
    <li>Coral Bay University Homecoming King, 2012</li>
  </ul>

  <h2 class="section-heading" style="top:542px">PROFESSIONAL AFFILIATIONS</h2>
  <ul class="bullets affiliations">
    <li>Member, Guild of Contemporary Composers (GCC)</li>
    <li>Member, National Alliance of Composers, Authors, and Publishers (NACAP)</li>
    <li>Member, Sound Recording Engineers League (SREL)</li>
    <li>Member, Delta Kappa Rho Fraternity, Incorporated</li>
  </ul>

  <h2 class="section-heading" style="top:675px">EXPERIENCE</h2>

  <section class="job" style="top:715px">
    <div class="job-head"><span class="job-title">Sound Engineer</span><span class="job-place">Bayside Film Works (BFW), Miami, FL, <small>May 2014 – Present</small></span></div>
    <ul class="bullets">
      <li>Edited and mixed recorded field audio to professional standards.</li>
      <li>Matched audio with motion picture video to create a seamless product.</li>
      <li>Recorded automated dialogue replacement (ADR) audio and integrated into<br>motion picture video project using Studio Suite 11.</li>
      <li>Recorded foley sound effects to be added to film, video, and other media<br>in post-production.</li>
      <li>Composed and recorded original music to accompany various video projects.</li>
    </ul>
  </section>

  <section class="job" style="top:908px">
    <div class="job-head"><span class="job-title">Sales Associate</span><span class="job-place">Brightmart Corp, Atlanta, GA, <small>May 2013 - Oct 2013</small></span></div>
    <p class="job-text">Provided customer service, maintained a clean and organized work environment,<br>assisted in sales, and performed cashier responsibilities.</p>
  </section>

  <section class="job" style="top:992px">
    <div class="job-head"><span class="job-title">On-site Promoter/Intern</span><span class="job-place">Georgia CAN,&nbsp; Atlanta, GA, <small>Jun 2012 - Aug 2012</small></span></div>
    <p class="job-text">(<span class="sc-text">Civic Action Network</span>) Promoted and advertised marketing campaigns and<br>managed office tasks such as setting up site maps, organizing and sorting<br>non-profit donations.</p>
  </section>

  <section class="job" style="top:1095px">
    <div class="job-head"><span class="job-title">Product Marketing Consultant</span><span class="job-place">Northline Marketing Inc, Atlanta, GA <small>Jun 2011 – Aug 2011</small></span></div>
    <p class="job-text">Conducted direct sales and marketing through establishing compelling value<br>propositions, overcoming objections, and closing the sale.</p>
  </section>
</main>
</body>
</html>
```